Business card design for IT consulting company

Looking for a simple, modern, clean business card design.
Open to reworking our existing logo.

Attached is our current business cards which we do not like.
Ideally double sided with something simple on the back.
Rectangle / Horizonal only.
No rounded edges on the card.
White as the dominate color is preferred.

Target Market(s)

clients, legal, oil & gas, medical, professionals

Industry/Entity Type

IT, tech, consulting

Contact Information for Business Card

Name, Title, email, phone, cell, website

Font styles to use
Sans Serif

Requirements
Must have
• Clean design
Should not have
• loud colors or unusual fonts, etc

```html
<!DOCTYPE html>
<html lang="en">
<head>
<meta charset="utf-8">
<title>Norvane Solutions – Business Card</title>
<link href="https://fonts.googleapis.com/css2?family=Lato:wght@400;900&display=swap" rel="stylesheet">
<style>
  :root {
    --bg: #e9e7e4;
    --card: #ffffff;
    --ink: #1f1f1f;
    --ink-soft: #3a3a3a;
    --accent: #3b4250;
    --rule: #9a9a9a;
  }
  * { box-sizing: border-box; margin: 0; padding: 0; }
  html, body { width: 1200px; height: 977px; overflow: hidden; }
  body {
    background: var(--bg);
    font-family: "Lato", Arial, sans-serif;
    color: var(--ink);
    position: relative;
  }
  .card {
    position: absolute;
    left: 270px;
    width: 660px;
    height: 377px;
    background: var(--card);
    box-shadow: 0 6px 18px rgba(0,0,0,0.12);
    overflow: hidden;
  }
  .card--back { top: 70px; }
  .card--front { top: 530px; }

  .brand { display: flex; align-items: center; gap: 16px; }
  .brand__square { background: var(--accent); flex: none; }
  .brand__name { font-weight: 900; color: var(--ink); line-height: 1; white-space: nowrap; }

  /* back */
  .card--back .brand {
    position: absolute; top: 118px; left: 0; right: 0; justify-content: center;
  }
  .card--back .brand__square { width: 78px; height: 78px; }
  .card--back .brand__name { font-size: 50px; }
  .website {
    position: absolute; top: 262px; left: 0; right: 0;
    text-align: center; font-size: 15px; letter-spacing: 6px; color: var(--ink-soft);
  }

  /* front */
  .card--front .brand { position: absolute; top: 72px; left: 150px; }
  .card--front .brand__square { width: 72px; height: 72px; }
  .card--front .brand__name { font-size: 40px; }

  .person {
    position: absolute; top: 200px; left: 20px; width: 302px; text-align: right;
    white-space: nowrap;
  }
  .person__name { font-weight: 900; font-size: 34px; letter-spacing: -0.5px; line-height: 1; }
  .person__title { font-size: 18px; color: var(--ink-soft); margin-top: 4px; }

  .divider {
    position: absolute; top: 184px; left: 342px; width: 1px; height: 86px; background: var(--rule);
  }
  .contact {
    position: absolute; top: 186px; left: 364px; list-style: none;
    font-size: 17px; color: var(--ink-soft); white-space: nowrap;
  }
  .contact li { display: flex; align-items: center; gap: 9px; height: 27px; }
  .contact svg { width: 15px; height: 15px; fill: none; stroke: var(--ink); stroke-width: 1.8; }

  .footer-band {
    position: absolute; left: 0; right: 0; bottom: 0; height: 9px; background: var(--accent);
  }
</style>
</head>
<body>
  <section class="card card--back" aria-label="Card back">
    <div class="brand">
      <span class="brand__square"></span>
      <span class="brand__name">Norvane</span>
    </div>
    <p class="website">WWW.NORVANE.CA</p>
  </section>

  <section class="card card--front" aria-label="Card front">
    <div class="brand">
      <span class="brand__square"></span>
      <span class="brand__name">Norvane Solutions</span>
    </div>

    <div class="person">
      <p class="person__name">DANIEL REYES</p>
      <p class="person__title">IT Consultant</p>
    </div>

    <div class="divider"></div>

    <ul class="contact">
      <li>
        <svg viewBox="0 0 16 16" aria-hidden="true"><path d="M4 2 L6.5 5 L5 7 C6 9 7 10 9 11 L11 9.5 L14 12 L12.5 14 C7 14 2 9 2 3.5 Z"/></svg>
        (800) 555-0142
      </li>
      <li>
        <svg viewBox="0 0 16 16" aria-hidden="true"><rect x="4" y="1.5" width="8" height="13" rx="1.5"/><line x1="7" y1="12" x2="9" y2="12"/></svg>
        (604) 555-0187
      </li>
      <li>
        <svg viewBox="0 0 16 16" aria-hidden="true"><rect x="1.5" y="3.5" width="13" height="9"/><polyline points="1.5,3.5 8,9 14.5,3.5"/></svg>
        daniel.reyes@norvane.ca
      </li>
    </ul>

    <div class="footer-band" aria-hidden="true"></div>
  </section>
</body>
</html>
```